Home page for local retail aggregator

About us: We are a new company that showcases beautiful products available at nearby retail stores. This homepage is meant to display the latest products featured on our site and also allow the user to search, browse with filters, and access their account details.

Currently, our home page looks a little bland. We want the focus of the site to remain on the featured photos and products but the design should be more cohesive. The most successful designs will make more subtle use of our colors, provide intuitive menu controls, and look visually stunning.

This homepage has a few sections:

Header:
-Top Section: will always remain at the top of the page. There should be space for our company name ”zAntelope”, a tagline, and a place for the menus.
-Menus: user must be able to find links for: “My profile” “My Products” “Add Product” “Preview store”
-Bottom section: this will scroll with the user and always remain at the top of the screen providing access to a search box, and filters for “location” “price” and retail categories.

Main Page:
-Each product featured is shown on a tile that includes a photo, title, price, name of store, has space to leave a comment, and include counters for "likes," comments, and "Pods"). “Pods” are bookmark folders. The user’s profile pic is also shown in miniature if they leave a comment.

The final version of the site must be delivered in a fully layered photoshop file and have versions demonstrating what the page will look like both when a user is logged-in and when logged-out.

Target Market(s)

Most of our users are female 18-45. Our customers are retail store owners who want their products to look attractive and professional.

Industry/Entity Type

Retail

Requirements
Must have
• Our logo must be present on the site (attached to project). You're welcome to change the colors in the header but it should look good with our logo.

For reference here are colors we're currently using:
Site text is in Dark Blue: RGB(10/23/47)
Logo color on business cards is light blue: (51/153/204)
Nice to have
• Would love to see new versions of the menus that are more modern and intuitive. Currently we just have links to each individual control. Putting these in a drop-down or re-arranging them would be nice.

```html
<!DOCTYPE html>
<html lang="en">
<head>
<meta charset="utf-8">
<title>zAntelope – Local Product Search and Discovery</title>
<link href="https://fonts.googleapis.com/css2?family=Lustria&display=swap" rel="stylesheet">
<style>
:root{
  --ink:#0a172f;
  --brand:#3399cc;
  --brand-deep:#1f6a9c;
  --nav-top:#2f86bd;
  --nav-bottom:#1b5e8f;
  --head-top:#dcebf8;
  --head-bottom:#a9cbe8;
  --price:#2a6896;
  --muted:#8a8a8a;
  --rule:#dedede;
  --frame:#e3e3e3;
  --well:#eeeeee;
  --stat-bar:rgba(40,40,40,.78);
  --foot:#0b1a28;
}
*{box-sizing:border-box;margin:0;padding:0}
html,body{width:1065px;height:1200px;overflow:hidden;background:#fff}
body{font-family:Arial,Helvetica,sans-serif;color:var(--ink);position:relative}

/* header */
.masthead{height:73px;background:linear-gradient(var(--head-top),var(--head-bottom));position:relative}
.brand{position:absolute;left:28px;top:10px;display:flex;align-items:center;gap:10px}
.brand-mark{width:44px;height:44px;border-radius:50%;background:var(--brand)}
.brand-name{font-family:'Lustria',serif;font-size:31px;color:var(--ink);line-height:1}
.brand-tagline{font-family:'Lustria',serif;font-size:9px;color:var(--ink);margin-top:4px}
.account-links{position:absolute;right:106px;top:31px;font-family:'Lustria',serif;font-style:italic;font-size:10px;color:var(--brand-deep)}
.account-links span{margin:0 3px}
.social{position:absolute;right:17px;top:24px;display:flex;gap:5px}
.social i{width:21px;height:21px;background:var(--brand-deep);border-radius:2px;display:block;box-shadow:0 2px 0 #9fb8cc}

.main-nav{height:33px;background:linear-gradient(var(--nav-top),var(--nav-bottom));position:relative;display:flex;align-items:center;padding-left:100px}
.menu-item{font-family:'Lustria',serif;font-size:11.5px;color:#fff;text-decoration:none;padding:0 12px;border-right:1px solid rgba(255,255,255,.25);line-height:18px;display:flex;align-items:center;gap:5px}
.menu-item.is-active{box-shadow:inset 0 -2px 0 #bfe0f3}
.caret{width:7px;height:5px;fill:#cfe6f4}

.filters{position:absolute;right:186px;top:6px;display:flex;gap:6px}
.filter{width:76px;height:22px;border-radius:11px;background:rgba(255,255,255,.16);border:1px solid rgba(255,255,255,.35);color:#fff;font-family:'Lustria',serif;font-size:9.5px;display:flex;align-items:center;justify-content:space-between;padding:0 9px}
.search{position:absolute;right:7px;top:5px;width:172px;height:24px;background:#fff;border:1px solid #c8d6e2;display:flex;align-items:center;justify-content:space-between;padding:0 7px}
.search span{font-family:'Lustria',serif;font-style:italic;font-size:9px;color:#999}

/* grid */
.wall{position:absolute;top:134px;left:15px;right:15px;height:950px;display:flex;gap:18px;overflow:hidden}
.column{width:245px;display:flex;flex-direction:column;gap:24px}
.tile{background:#fff;border:2px solid var(--frame);padding:6px 7px 7px;position:relative}
.tile::after{content:"";position:absolute;left:20px;right:20px;bottom:-9px;height:8px;background:radial-gradient(ellipse at top,rgba(0,0,0,.18),rgba(0,0,0,0) 70%)}
.photo{position:relative;height:178px}
.photo.tall{height:238px}
.photo .fill{position:absolute;inset:0}
.fill.candle{background:linear-gradient(135deg,#3f5e2c,#c9c6b7 55%,#6a7a3a)}
.fill.corkscrew{background:linear-gradient(135deg,#f4f4f4,#e6e6e6 50%,#d9e4ea)}
.fill.chocolate{background:linear-gradient(135deg,#6b3d1c,#9b5d2f 50%,#5a3216)}
.fill.kurta{background:linear-gradient(180deg,#4a3524,#b59a70 60%,#8c7450)}
.stats{position:absolute;left:0;right:0;bottom:0;height:22px;background:var(--stat-bar);display:flex;align-items:center;gap:13px;padding-left:9px;color:#fff;font-size:9px}
.stats span{display:flex;align-items:center;gap:4px}
.stats svg{width:11px;height:11px;fill:#fff}
.title-row{display:flex;justify-content:space-between;align-items:flex-start;gap:6px;padding:6px 3px 0}
.title{font-family:'Lustria',serif;font-size:10.5px;font-weight:normal;color:var(--ink);white-space:nowrap;padding-top:1px}
.price{font-family:'Lustria',serif;font-size:17px;color:var(--price);padding-right:8px;flex:none}
.store{font-family:'Lustria',serif;font-style:italic;font-size:9px;color:var(--muted);padding:0 3px;margin-top:-5px}
.comments{list-style:none;margin-top:7px}
.comment{display:flex;gap:6px;padding:3px 3px 6px;border-bottom:1px solid var(--rule);margin-bottom:7px;font-size:8.5px;line-height:11px;color:var(--muted)}
.comment b{font-weight:normal;color:#222}
.avatar{width:29px;height:29px;flex:none;border:1px solid #ccc;background:linear-gradient(135deg,#caa27a,#8a6a4a)}
.avatar.b{background:linear-gradient(135deg,#e2c4a8,#b88c6a)}
.avatar.c{background:linear-gradient(135deg,#5a4a4a,#2a2020)}
.avatar.d{background:linear-gradient(135deg,#5a5550,#1e1c1a)}
.all{text-align:center;font-size:8.5px;color:#222;margin:4px 0 7px}
.reply{background:var(--well);padding:6px 8px;display:flex}
.reply .field{flex:1;height:19px;background:#fff;border:1px solid #d6d6d6;border-right:none}
.reply button{width:50px;height:19px;border:none;border-radius:2px;background:linear-gradient(#3a8bc0,#1d5f90);color:#fff;font-size:9px;font-family:Arial,sans-serif}

/* footer */
.site-foot{position:absolute;left:0;right:0;bottom:0;height:47px;background:var(--foot);color:#fff;font-size:8.5px;display:flex;align-items:center;justify-content:space-between;padding:0 64px 0 62px}
</style>
</head>
<body>

<svg width="0" height="0" style="position:absolute">
  <symbol id="i-comment" viewBox="0 0 12 12"><path d="M1 2h10v6H6l-3 3V8H1z"/></symbol>
  <symbol id="i-like" viewBox="0 0 12 12"><path d="M6 11L1.2 6.2A2.8 2.8 0 016 2.4a2.8 2.8 0 014.8 3.8z"/></symbol>
  <symbol id="i-pod" viewBox="0 0 12 12"><path d="M3 1h6v10H3zM4.3 2.3v7.4h3.4V2.3z" fill-rule="evenodd"/></symbol>
  <symbol id="i-caret" viewBox="0 0 8 5"><path d="M0 0h8L4 5z"/></symbol>
</svg>

<header>
  <div class="masthead">
    <div class="brand">
      <span class="brand-mark"></span>
      <div>
        <div class="brand-name">zAntelope</div>
        <div class="brand-tagline">Local Product Search and Discovery</div>
      </div>
    </div>
    <div class="account-links">Logout<span>-</span>My Inventory<span>-</span>My Profile</div>
    <div class="social"><i></i><i></i><i></i></div>
  </div>
  <nav class="main-nav">
    <a class="menu-item is-active" href="#">MY PROFILE <svg class="caret"><use href="#i-caret"/></svg></a>
    <a class="menu-item" href="#">MY PRODUCTS <svg class="caret"><use href="#i-caret"/></svg></a>
    <a class="menu-item" href="#">ADD PRODUCT</a>
    <a class="menu-item" href="#">PREVIEW STORE</a>
    <div class="filters">
      <span class="filter">Location <svg class="caret"><use href="#i-caret"/></svg></span>
      <span class="filter">Price <svg class="caret"><use href="#i-caret"/></svg></span>
      <span class="filter">Category <svg class="caret"><use href="#i-caret"/></svg></span>
    </div>
    <div class="search">
      <span>Search</span>
      <svg width="14" height="14" viewBox="0 0 14 14"><circle cx="5.5" cy="5.5" r="4" fill="none" stroke="#bbb" stroke-width="1.6"/><path d="M8.5 8.5l4 4" stroke="#bbb" stroke-width="2"/></svg>
    </div>
  </nav>
</header>

<main class="wall">
  <div class="column">
    <article class="tile">
      <div class="photo"><div class="fill candle" role="img" aria-label="Sunflower candle box on a garden table"></div>
        <div class="stats"><span><svg><use href="#i-comment"/></svg>20</span><span><svg><use href="#i-like"/></svg>65</span><span><svg><use href="#i-pod"/></svg>96</span></div></div>
      <div class="title-row"><h3 class="title">Sweet sunflower candle</h3><span class="price">$30</span></div>
      <p class="store">Minimal</p>
      <ul class="comments">
        <li class="comment"><span class="avatar" role="img" aria-label="Commenter profile photo"></span><p><b>Nora Pell</b> onto so true.</p></li>
        <li class="comment"><span class="avatar b" role="img" aria-label="Commenter profile photo"></span><p><b>Dev Marlow</b> @patty brenner..haha..It's you!</p></li>
        <li class="comment"><span class="avatar c" role="img" aria-label="Commenter profile photo"></span><p><b>Sam Ortega</b> i actually have this tattoo on my back and i got it for its beauty and it has alot of meaning to me. feathers and birds means to be free spirited.</p></li>
        <li class="comment"><span class="avatar d" role="img" aria-label="Commenter profile photo"></span><p><b>Leo Finch</b>&nbsp; this is very creative! nice artwork</p></li>
      </ul>
      <p class="all">All 10 comments....</p>
      <div class="reply"><span class="field"></span><button>Submit</button></div>
    </article>
    <article class="tile">
      <div class="photo"><div class="fill kurta" role="img" aria-label="Man wearing an embroidered kurta"></div>
        <div class="stats"><span><svg><use href="#i-comment"/></svg>20</span><span><svg><use href="#i-like"/></svg>65</span><span><svg><use href="#i-pod"/></svg>96</span></div></div>
      <div class="title-row"><h3 class="title">Embroidered Mens Kurta Pyjama</h3><span class="price">$30</span></div>
      <p class="store">Minimal</p>
      <ul class="comments">
        <li class="comment"><span class="avatar" role="img" aria-label="Commenter profile photo"></span><p><b>Nora Pell</b> onto so true.</p></li>
        <li class="comment"><span class="avatar b" role="img" aria-label="Commenter profile photo"></span><p><b>Dev Marlow</b> @patty brenner..haha..It's you!</p></li>
        <li class="comment"><span class="avatar d" role="img" aria-label="Commenter profile photo"></span><p><b>Leo Finch</b>&nbsp; this is very creative! nice artwork</p></li>
      </ul>
      <p class="all">All 10 comments....</p>
      <div class="reply"><span class="field"></span><button>Submit</button></div>
    </article>
  </div>

  <div class="column">
    <article class="tile">
      <div class="photo tall"><div class="fill corkscrew" role="img" aria-label="Four colourful parrot-shaped corkscrews"></div>
        <div class="stats"><span><svg><use href="#i-comment"/></svg>20</span><span><svg><use href="#i-like"/></svg>65</span><span><svg><use href="#i-pod"/></svg>96</span></div></div>
      <div class="title-row"><h3 class="title">Parrot corkscrew</h3><span class="price">$30</span></div>
      <p class="store">Minimal</p>
      <ul class="comments">
        <li class="comment"><span class="avatar" role="img" aria-label="Commenter profile photo"></span><p><b>Nora Pell</b> onto so true.</p></li>
        <li class="comment"><span class="avatar b" role="img" aria-label="Commenter profile photo"></span><p><b>Dev Marlow</b> @patty brenner..haha..It's you!</p></li>
        <li class="comment"><span class="avatar c" role="img" aria-label="Commenter profile photo"></span><p><b>Sam Ortega</b> i actually have this tattoo on my back and i got it for its beauty and it has alot of meaning to me. feathers and birds means to be free spirited.</p></li>
        <li class="comment"><span class="avatar d" role="img" aria-label="Commenter profile photo"></span><p><b>Leo Finch</b>&nbsp; this is very creative! nice artwork</p></li>
      </ul>
      <p class="all">All 10 comments....</p>
      <div class="reply"><span class="field"></span><button>Submit</button></div>
    </article>
    <article class="tile">
      <div class="photo"><div class="fill chocolate" role="img" aria-label="Close-up of a milk chocolate bar"></div>
        <div class="stats"><span><svg><use href="#i-comment"/></svg>20</span><span><svg><use href="#i-like"/></svg>65</span><span><svg><use href="#i-pod"/></svg>96</span></div></div>
      <div class="title-row"><h3 class="title">Choclate</h3><span class="price">$30</span></div>
      <p class="store">Minimal</p>
      <ul class="comments">
        <li class="comment"><span class="avatar" role="img" aria-label="Commenter profile photo"></span><p><b>Nora Pell</b> onto so true.</p></li>
        <li class="comment"><span class="avatar b" role="img" aria-label="Commenter profile photo"></span><p><b>Dev Marlow</b> @patty brenner..haha..It's you!</p></li>
      </ul>
      <p class="all">All 10 comments....</p>
      <div class="reply"><span class="field"></span><button>Submit</button></div>
    </article>
  </div>

  <div class="column">
    <article class="tile">
      <div class="photo"><div class="fill chocolate" role="img" aria-label="Close-up of a milk chocolate bar"></div>
        <div class="stats"><span><svg><use href="#i-comment"/></svg>20</span><span><svg><use href="#i-like"/></svg>65</span><span><svg><use href="#i-pod"/></svg>96</span></div></div>
      <div class="title-row"><h3 class="title">Choclate</h3><span class="price">$30</span></div>
      <p class="store">Minimal</p>
      <ul class="comments">
        <li class="comment"><span class="avatar" role="img" aria-label="Commenter profile photo"></span><p><b>Nora Pell</b> onto so true.</p></li>
        <li class="comment"><span class="avatar b" role="img" aria-label="Commenter profile photo"></span><p><b>Dev Marlow</b> @patty brenner..haha..It's you!</p></li>
      </ul>
      <p class="all">All 10 comments....</p>
      <div class="reply"><span class="field"></span><button>Submit</button></div>
    </article>
    <article class="tile">
      <div class="photo tall"><div class="fill corkscrew" role="img" aria-label="Four colourful parrot-shaped corkscrews"></div>
        <div class="stats"><span><svg><use href="#i-comment"/></svg>20</span><span><svg><use href="#i-like"/></svg>65</span><span><svg><use href="#i-pod"/></svg>96</span></div></div>
      <div class="title-row"><h3 class="title">Parrot corkscrew</h3><span class="price">$30</span></div>
      <p class="store">Minimal</p>
      <ul class="comments">
        <li class="comment"><span class="avatar" role="img" aria-label="Commenter profile photo"></span><p><b>Nora Pell</b> onto so true.</p></li>
        <li class="comment"><span class="avatar b" role="img" aria-label="Commenter profile photo"></span><p><b>Dev Marlow</b> @patty brenner..haha..It's you!</p></li>
        <li class="comment"><span class="avatar c" role="img" aria-label="Commenter profile photo"></span><p><b>Sam Ortega</b> i actually have this tattoo on my back and i got it for its beauty and it has alot of meaning to me. feathers and birds means to be free spirited.</p></li>
        <li class="comment"><span class="avatar d" role="img" aria-label="Commenter profile photo"></span><p><b>Leo Finch</b>&nbsp; this is very creative! nice artwork</p></li>
      </ul>
      <p class="all">All 10 comments....</p>
      <div class="reply"><span class="field"></span><button>Submit</button></div>
    </article>
  </div>

  <div class="column">
    <article class="tile">
      <div class="photo"><div class="fill kurta" role="img" aria-label="Man wearing an embroidered kurta"></div>
        <div class="stats"><span><svg><use href="#i-comment"/></svg>20</span><span><svg><use href="#i-like"/></svg>65</span><span><svg><use href="#i-pod"/></svg>96</span></div></div>
      <div class="title-row"><h3 class="title">Embroidered Mens Kurta Pyjama</h3><span class="price">$30</span></div>
      <p class="store">Minimal</p>
      <ul class="comments">
        <li class="comment"><span class="avatar" role="img" aria-label="Commenter profile photo"></span><p><b>Nora Pell</b> onto so true.</p></li>
        <li class="comment"><span class="avatar b" role="img" aria-label="Commenter profile photo"></span><p><b>Dev Marlow</b> @patty brenner..haha..It's you!</p></li>
        <li class="comment"><span class="avatar d" role="img" aria-label="Commenter profile photo"></span><p><b>Leo Finch</b>&nbsp; this is very creative! nice artwork</p></li>
      </ul>
      <p class="all">All 10 comments....</p>
      <div class="reply"><span class="field"></span><button>Submit</button></div>
    </article>
    <article class="tile">
      <div class="photo"><div class="fill candle" role="img" aria-label="Sunflower candle box on a garden table"></div>
        <div class="stats"><span><svg><use href="#i-comment"/></svg>20</span><span><svg><use href="#i-like"/></svg>65</span><span><svg><use href="#i-pod"/></svg>96</span></div></div>
      <div class="title-row"><h3 class="title">Sweet sunflower candle</h3><span class="price">$30</span></div>
      <p class="store">Minimal</p>
      <ul class="comments">
        <li class="comment"><span class="avatar" role="img" aria-label="Commenter profile photo"></span><p><b>Nora Pell</b> onto so true.</p></li>
        <li class="comment"><span class="avatar b" role="img" aria-label="Commenter profile photo"></span><p><b>Dev Marlow</b> @patty brenner..haha..It's you!</p></li>
        <li class="comment"><span class="avatar c" role="img" aria-label="Commenter profile photo"></span><p><b>Sam Ortega</b> i actually have this tattoo on my back and i got it for its beauty and it has alot of meaning to me. feathers and birds means to be free spirited.</p></li>
        <li class="comment"><span class="avatar d" role="img" aria-label="Commenter profile photo"></span><p><b>Leo Finch</b>&nbsp; this is very creative! nice artwork</p></li>
      </ul>
      <p class="all">All 10 comments....</p>
      <div class="reply"><span class="field"></span><button>Submit</button></div>
    </article>
  </div>
</main>

<footer class="site-foot">
  <span>About I Contact I Help I Privacy I Terms</span>
  <span>© 2012 Copyright zAntelope | All Rights Reserved.</span>
</footer>

</body>
</html>
```